Haulage company, lets use ruby red white and some 3rd color for web design. and Alder Croft Transport logo

Target Market(s)

Transport industry

Industry/Entity Type

transport

Number of Pages Required

2 page

Requirements
Must have
• Logo

```html
<!DOCTYPE html>
<html lang="en">
<head>
<meta charset="utf-8">
<title>Alder Croft Transport</title>
<link href="https://fonts.googleapis.com/css2?family=Poppins:ital,wght@0,400;0,500;0,600;0,700;1,400&display=swap" rel="stylesheet">
<style>
:root{
  --ruby:#8c1a2c;
  --ruby-dark:#6e1220;
  --ink:#1d1d1f;
  --text:#555a60;
  --mist:#eef0f5;
  --night:#232325;
  --white:#ffffff;
}
*{margin:0;padding:0;box-sizing:border-box}
html,body{width:1200px;height:4946px;overflow:hidden}
body{position:relative;font-family:'Poppins',sans-serif;color:var(--ink);background:var(--white)}
.abs{position:absolute}
.accent{color:var(--ruby)}
.section-title{position:absolute;left:0;width:1200px;text-align:center;font-weight:600;font-size:39px;letter-spacing:.5px;text-transform:uppercase;line-height:1}

/* hero */
.hero{position:absolute;left:0;top:0;width:1200px;height:682px;background:linear-gradient(100deg,#1a1a1c 0%,#2c2b2e 40%,#4a3a3e 60%,#6b6a70 80%,#3a3a3e 100%)}
.hero-photo{position:absolute;inset:0;background:radial-gradient(ellipse at 70% 55%,rgba(200,195,200,.35),transparent 55%),radial-gradient(ellipse at 55% 70%,rgba(140,26,44,.45),transparent 40%)}
.hero-shade{position:absolute;inset:0;background:linear-gradient(90deg,rgba(0,0,0,.55) 0%,rgba(0,0,0,.2) 55%,rgba(0,0,0,0) 100%)}
.brand{position:absolute;display:flex;align-items:center;gap:16px;color:var(--white);font-weight:600}
.brand-mark{border-radius:50%;background:var(--ruby)}
.brand-name{line-height:1.15}
.brand-name span{display:block}
.topbar{position:absolute;right:110px;top:18px;display:flex;gap:14px;color:var(--white);font-size:16px;align-items:center}
.topbar svg{vertical-align:-2px;margin-right:6px}
.nav{position:absolute;right:110px;top:64px;display:flex;gap:38px;color:var(--white);font-size:16px}
.nav .current{color:#e0475c}
.hero-title{position:absolute;left:110px;top:186px;color:var(--white);font-weight:700;font-size:79px;line-height:86px;letter-spacing:1px}
.hero-rule{position:absolute;left:110px;top:382px;width:504px;height:4px;background:var(--white)}
.hero-sub{position:absolute;left:108px;top:408px;color:var(--white);font-size:23px;font-weight:500}
.btn{position:absolute;border-radius:40px;font-weight:600;font-size:18px;display:flex;align-items:center;justify-content:center;text-transform:uppercase}
.btn-ruby{background:var(--ruby);color:var(--white)}
.btn-white{background:var(--white);color:var(--ink)}

/* welcome */
.welcome-photo{position:absolute;left:45px;top:736px;width:488px;height:488px;border-radius:50%;background:linear-gradient(150deg,#9fc6ec 0%,#d8dde3 45%,#f2f2f2 60%,#8c1a2c 80%,#3d3d40 100%)}
.welcome-title{position:absolute;left:630px;top:776px;font-size:40px;font-weight:600;line-height:53px;text-transform:uppercase}
.body-copy{font-size:16px;line-height:27.5px;color:var(--text)}
.welcome-copy{position:absolute;left:630px;top:903px;width:470px}
.welcome-note{position:absolute;left:630px;top:1092px;font-size:16px;font-weight:600}
.signature{position:absolute;left:624px;top:1140px;width:260px;height:68px;border-radius:4px;background:linear-gradient(90deg,rgba(140,26,44,.18),rgba(140,26,44,.06))}

/* services */
.services{position:absolute;left:0;top:1315px;width:1200px;height:720px;background:var(--mist)}
.card{position:absolute;top:175px;width:311px;height:459px;background:var(--white);box-shadow:0 2px 8px rgba(0,0,0,.06)}
.card-photo{height:227px}
.card h3{position:absolute;left:20px;top:248px;width:280px;font-size:21px;font-weight:500;line-height:28px;color:var(--ink)}
.card p{position:absolute;left:22px;top:317px;width:275px;font-size:15.5px;line-height:25px;color:var(--text)}
.card .more{position:absolute;left:22px;top:413px;font-size:16px;font-weight:600;color:var(--ruby)}
.card-fade{position:absolute;left:1112px;top:175px;width:88px;height:459px;background:linear-gradient(90deg,rgba(238,240,245,.55),rgba(238,240,245,.9))}
.round-btn{position:absolute;border-radius:50%;background:var(--white);display:flex;align-items:center;justify-content:center;box-shadow:0 2px 6px rgba(0,0,0,.15)}

/* why */
.why-sub{position:absolute;left:0;top:2193px;width:1200px;text-align:center}
.why-photo{position:absolute;left:0;top:2440px;width:1200px;height:521px;background:linear-gradient(180deg,#ffffff 0%,#d9e3ec 22%,#6d8aa6 48%,#8a8f96 62%,#cfd2d6 78%,#5d5f64 100%)}
.feature{position:absolute;top:2292px;width:240px;text-align:center;font-size:19px;font-weight:500;line-height:28px}
.feature svg{display:block;margin:0 auto 18px}

/* testimonials */
.client-badge{position:absolute;left:515px;top:3110px;width:169px;height:144px;background:var(--white);box-shadow:0 2px 10px rgba(0,0,0,.07);display:flex;flex-direction:column;align-items:center;justify-content:center;gap:10px;font-size:18px;font-weight:600;color:var(--ink)}
.client-badge i{width:34px;height:34px;border-radius:50%;background:var(--ink);display:block}
.quote{position:absolute;left:170px;top:3263px;width:860px;text-align:center;font-style:italic;font-size:20px;line-height:33px;color:#444}
.quote-name{position:absolute;left:0;top:3424px;width:1200px;text-align:center;font-size:19px;font-weight:500}

/* cta */
.cta{position:absolute;left:0;top:3552px;width:1200px;height:445px;background:linear-gradient(100deg,#7a1424 0%,#962337 45%,#a23a4b 70%,#8c1a2c 100%)}
.cta-title{position:absolute;left:0;top:90px;width:1200px;text-align:center;color:var(--white);font-weight:600;font-size:39px;line-height:52px}
.cta-copy{position:absolute;left:0;top:210px;width:1200px;text-align:center;color:var(--white);font-size:16px;line-height:27px}

/* location */
.loc-title{position:absolute;left:110px;top:4098px;font-size:40px;font-weight:600;line-height:52px;text-transform:uppercase}
.loc-copy{position:absolute;left:110px;top:4275px;width:470px}
.map{position:absolute;left:682px;top:4003px;width:326px;height:490px;border-radius:6px;background:linear-gradient(160deg,#f1f1f1 0%,#d8d8d8 30%,#9a2a3c 45%,#8c1a2c 100%)}

/* footer */
.footer{position:absolute;left:0;top:4554px;width:1200px;height:392px;background:var(--night);color:var(--white)}
.footer h4{position:absolute;top:73px;font-size:19px;font-weight:600}
.footer ul{position:absolute;list-style:none;font-size:15.5px;line-height:29px}
.contact-line{position:absolute;left:789px;font-size:16px;line-height:24px;display:flex;gap:12px}
.contact-line svg{flex:none;margin-top:4px}
.footer-rule{position:absolute;left:110px;top:288px;width:980px;height:1px;background:#4a4a4e}
.copyright{position:absolute;left:110px;top:321px;font-size:15.5px}
.social{position:absolute;top:309px;width:46px;height:46px;border:1.5px solid var(--white);border-radius:50%}
</style>
</head>
<body>

<header class="hero">
  <div class="hero-photo" role="img" aria-label="Two red and white articulated lorries parked at night"></div>
  <div class="hero-shade"></div>
  <div class="brand" style="left:110px;top:30px">
    <span class="brand-mark" style="width:72px;height:72px"></span>
    <span class="brand-name"><span style="font-size:25px">ALDER CROFT</span><span style="font-size:18px;letter-spacing:5px">Transport</span></span>
  </div>
  <div class="topbar">
    <span><svg width="14" height="14" viewBox="0 0 24 24" fill="#e0475c"><path d="M6.6 10.8a15 15 0 0 0 6.6 6.6l2.2-2.2c.3-.3.7-.4 1-.2 1.1.4 2.3.6 3.6.6.6 0 1 .4 1 1V20c0 .6-.4 1-1 1A17 17 0 0 1 3 4c0-.6.4-1 1-1h3.5c.6 0 1 .4 1 1 0 1.3.2 2.5.6 3.6.1.3 0 .7-.2 1z"/></svg>1 800 555 0142</span>
    <span>|</span>
    <span><svg width="15" height="12" viewBox="0 0 24 18" fill="#e0475c"><path d="M0 0h24v18H0z"/><path d="M0 0l12 9 12-9" stroke="#fff" stroke-width="2" fill="none"/></svg>info@aldercroft-haulage.com</span>
  </div>
  <nav class="nav"><span class="current">Home</span><span>About Us</span><span>Services</span><span>Blog</span><span>Contact Us</span></nav>
  <h1 class="hero-title">ALDER CROFT<br>TRANSPORT</h1>
  <div class="hero-rule"></div>
  <p class="hero-sub">We are Haulage Transport services company</p>
  <div class="btn btn-ruby" style="left:110px;top:486px;width:188px;height:63px">Get a quote</div>
</header>

<section>
  <div class="welcome-photo" role="img" aria-label="White lorry with ruby red cab and refrigerated trailer"></div>
  <h2 class="welcome-title">Welcome to<br><span class="accent">Alder Croft Transport</span></h2>
  <p class="welcome-copy body-copy">Lorem ipsum dolor sit amet, consectetur adipiscing elitlui, sed do eiusmod tempor incididunt ut labore et dol hyore magna aliqua. Ut enim ad minim veniam, quis nostrtuud exercitation ullamco laboris nisi ut aliquip ex ea commio do consequat. Duis aute irure dolor in reprehend iklerit in voluptate velit esse cillum dolore.</p>
  <p class="welcome-note">FOR A COMPETITIVE QUOTE SPEAK TO US DIRECT TODAY.</p>
  <div class="signature" role="img" aria-label="Handwritten signature of the company director"></div>
</section>

<section class="services">
  <h2 class="section-title" style="top:82px">Our <span class="accent">Services</span></h2>
  <article class="card" style="left:110px">
    <div class="card-photo" role="img" aria-label="Two lorries parked side by side" style="background:linear-gradient(180deg,#e7e8ea,#b9b4b7 60%,#8c1a2c 85%,#9a9a9a)"></div>
    <h3>Full Container Load (FCL) Haulage Services</h3>
    <p>Excepteur sint occaecat cupidat at non proident, sunt in culpa qui officia deserunt molli.</p>
    <span class="more">READ MORE</span>
  </article>
  <article class="card" style="left:444px">
    <div class="card-photo" role="img" aria-label="Lorries on a coastal road under a blue sky" style="background:linear-gradient(180deg,#5b8fd0,#cfe0f2 45%,#e6e6e6 65%,#4c6f90 80%,#6a6a6a)"></div>
    <h3>Full Truck Load (FTL) Haulage Services</h3>
    <p>Excepteur sint occaecat cupidat at non proident, sunt in culpa qui officia deserunt molli.</p>
    <span class="more">READ MORE</span>
  </article>
  <article class="card" style="left:778px">
    <div class="card-photo" role="img" aria-label="Front of a lorry cab at dusk" style="background:linear-gradient(180deg,#8fb1d8,#e9e2d8 45%,#d8d8d8 60%,#8c1a2c 85%,#555)"></div>
    <h3>Cross-docking<br>Services</h3>
    <p>Excepteur sint occaecat cupidat at non proident, sunt in culpa qui officia deserunt molli.</p>
    <span class="more">READ MORE</span>
  </article>
  <article class="card" style="left:1112px">
    <div class="card-photo" role="img" aria-label="Lorry trailer in a yard" style="background:linear-gradient(180deg,#9a9a9c,#d8d8d8)"></div>
    <h3>Customs Clearance</h3>
    <p>Excepteur sint occaecat cupidat at non proident, sunt in culpa qui officia deserunt molli.</p>
    <span class="more">READ MORE</span>
  </article>
  <div class="card-fade"></div>
  <div class="round-btn" style="left:1072px;top:370px;width:54px;height:54px">
    <svg width="14" height="18" viewBox="0 0 14 18"><path d="M3 2l8 7-8 7" stroke="#222" stroke-width="2.4" fill="none"/></svg>
  </div>
</section>

<section>
  <div class="why-photo" role="img" aria-label="Two refrigerated lorries driving along a coastal road"></div>
  <h2 class="section-title" style="top:2128px">Why choose <span class="accent">Alder Croft Transport</span></h2>
  <p class="why-sub body-copy">Lorem ipsum dolor sit amet, consectetur adipiscing elitlui, sed do eiusmod tempor incididunt<br>ut labore et dol hyore magna aliquenim ad minim veniam, quis nostrtuu.</p>
  <div class="feature" style="left:84px">
    <svg width="96" height="72" viewBox="0 0 96 72" fill="none" stroke="#8c1a2c" stroke-width="3"><path d="M22 12h40v40H22zM62 26h16l10 14v12H62"/><circle cx="34" cy="56" r="7" fill="#fff"/><circle cx="76" cy="56" r="7" fill="#fff"/><path d="M4 22h14M8 32h10M2 42h16"/></svg>
    High-Volume<br>Shipping Solutions
  </div>
  <div class="feature" style="left:348px">
    <svg width="96" height="92" viewBox="0 0 96 92" fill="none" stroke="#8c1a2c" stroke-width="3"><path d="M30 4l22 8v18c0 14-10 22-22 28C18 52 8 44 8 30V12z"/><rect x="24" y="26" width="12" height="10"/><path d="M56 44h18l10 14v14H40v-10M48 72h-8"/><circle cx="52" cy="76" r="7" fill="#fff"/><circle cx="78" cy="76" r="7" fill="#fff"/></svg>
    Safe and efficiency<br>transport
  </div>
  <div class="feature" style="left:612px">
    <svg width="96" height="92" viewBox="0 0 96 92" fill="none" stroke="#8c1a2c" stroke-width="3"><circle cx="34" cy="22" r="10"/><circle cx="34" cy="22" r="4"/><circle cx="66" cy="14" r="8"/><path d="M6 54l14-8 16 4 10 8M90 54l-14-8-16 4-14 10 6 6 14-8 14 12M20 46l-14 16M76 46l14 16M32 70l8 8M26 64l8 8"/></svg>
    Customised<br>Services
  </div>
  <div class="feature" style="left:876px">
    <svg width="80" height="100" viewBox="0 0 80 100" fill="none" stroke="#8c1a2c" stroke-width="3"><rect x="10" y="4" width="60" height="70"/><path d="M22 18h36M22 28h36"/><circle cx="40" cy="56" r="11"/><path d="M32 66l-6 28 14-8 14 8-6-28"/></svg>
    Certified
  </div>
</section>

<section>
  <h2 class="section-title" style="top:3044px">Client <span class="accent">Testimonials</span></h2>
  <div class="client-badge"><i></i>Northgate Foods</div>
  <p class="quote">“ Nemo enim ipsam voluptatem quia voluptas sit aspernatur aut odit aut fugit, sed quia consequuntur magni dolores eos qui ratione voluptatem sequi nesciunt. Neque porro quisquam est, qui dolorem ipsum quia dolor sit amet, consectetur, adipisci velit, sed quia non numquam eius modi tempor. ”</p>
  <p class="quote-name">- Peter Lowell</p>
</section>

<section class="cta">
  <div class="abs" role="img" aria-label="Faded lorry trailer behind a ruby overlay" style="inset:0;background:linear-gradient(90deg,rgba(255,255,255,0),rgba(255,255,255,.08) 60%,rgba(255,255,255,0))"></div>
  <h2 class="cta-title">READY TO EXPERIENCE<br>OUR EXCEPTIONAL SERVICES?</h2>
  <p class="cta-copy">Lorem ipsum dolor sit amet, consectetur adipiscing elitlui, sed do eiusmod tempor incididunt<br>ut labore et dol hyore magna aliquenim ad minim veniam, quis nostrtuu.</p>
  <div class="btn btn-white" style="left:507px;top:300px;width:186px;height:61px">Get a quote</div>
</section>

<div class="round-btn" style="left:545px;top:3528px;width:44px;height:44px"><svg width="10" height="14" viewBox="0 0 10 14"><path d="M8 1L2 7l6 6" stroke="#222" stroke-width="2" fill="none"/></svg></div>
<div class="round-btn" style="left:609px;top:3528px;width:44px;height:44px"><svg width="10" height="14" viewBox="0 0 10 14"><path d="M2 1l6 6-6 6" stroke="#222" stroke-width="2" fill="none"/></svg></div>

<section>
  <h2 class="loc-title">Strategically<br>located <span class="accent">for your<br>convenience</span></h2>
  <p class="loc-copy body-copy">Lorem ipsum dolor sit amet, consectetur adipiscing elitlui, sed do eiusmod tempor incididunt ut labore et dol hyore magna aliqua. Ut enim ad minim veniam, quis nostrtuud exercitation ullamco laboris nisi ut aliquip ex ea commio do consequat. Duis aute irure dolor in reprehend iklerit in voluptate velit esse cillum dolore.</p>
  <div class="map" role="img" aria-label="Map of the British Isles with depot locations marked"></div>
</section>

<footer class="footer">
  <div class="brand" style="left:110px;top:73px">
    <span class="brand-mark" style="width:96px;height:96px"></span>
    <span class="brand-name"><span style="font-size:33px">ALDER CROFT</span><span style="font-size:24px;letter-spacing:6px">Transport</span></span>
  </div>
  <h4 style="left:566px">Quick Links</h4>
  <ul style="left:566px;top:112px"><li>Home</li><li>About Us</li><li>Services</li><li>Blog</li><li>Contact Us</li></ul>
  <h4 style="left:789px">Contact Information</h4>
  <div class="contact-line" style="top:113px"><svg width="12" height="16" viewBox="0 0 12 16" fill="#fff"><path d="M6 0a6 6 0 0 0-6 6c0 4.5 6 10 6 10s6-5.5 6-10a6 6 0 0 0-6-6zm0 8.5A2.5 2.5 0 1 1 6 3.5a2.5 2.5 0 0 1 0 5z"/></svg><span>48 Kestrel Lane, Hampton<br>Vale</span></div>
  <div class="contact-line" style="top:182px"><svg width="14" height="14" viewBox="0 0 24 24" fill="#fff"><path d="M6.6 10.8a15 15 0 0 0 6.6 6.6l2.2-2.2c.3-.3.7-.4 1-.2 1.1.4 2.3.6 3.6.6.6 0 1 .4 1 1V20c0 .6-.4 1-1 1A17 17 0 0 1 3 4c0-.6.4-1 1-1h3.5c.6 0 1 .4 1 1 0 1.3.2 2.5.6 3.6.1.3 0 .7-.2 1z"/></svg><span>1 800 555 0142</span></div>
  <div class="contact-line" style="top:230px"><svg width="15" height="12" viewBox="0 0 24 18" fill="#fff"><path d="M0 0h24v18H0z"/><path d="M0 0l12 9 12-9" stroke="#232325" stroke-width="2" fill="none"/></svg><span>hello@aldercroft-haulage.com</span></div>
  <div class="footer-rule"></div>
  <p class="copyright">© Copyright 2024, Alder Croft Transport. All Rights Reserved</p>
  <span class="social" style="left:939px" aria-label="Social profile"></span>
  <span class="social" style="left:991px" aria-label="Social profile"></span>
  <span class="social" style="left:1043px" aria-label="Social profile"></span>
</footer>

</body>
</html>
```